Brennick Bros (logo) and Premium Tovelin Potatoes (package design)

Design a brand logo for Brennick Bros, and create a package design (face panel only) for a bag of Premium Tovelin Potatoes.

Attached is a quick concept to give you a rough idea. However, we would like it be more unique and not so common as the idea shown. It needs to be PREMIUM as these are slightly higher priced potatoes. And the packaging needs to look different than the typical potato bags. The brand story is the Brennick brothers have been farming potatoes in Ireland for four generations. They are now creating their own brand and will market the best potatoes available in Ireland (shape, no blemishes, color, taste, size, etc.). The type of potato is Tovelin.

There will be a window in the front panel to show the product behind netting. Use the other image (Dunholt Potatoes) as a guide to the bag shape (face panel only) and location of the window.

The bag can be any color, and you can design with any photos/images/etc. that are royalty free. The tear strip across the top can be any color, too.

Reason: Time extended. But please submits within the next day or two at the latest due to print deadline. Thanks!

Moms with families

Farming

Serif

• Brennick Bros logo
• Premium Tovelin Potatoes (copy)
• Window to show product (potatoes)
• Bag Net Weight: 10 kg
• Dimensions: 22 inches high and 10.5 wide
• Brand name/logo must be readable and large on the bag
• Bag should stand out and be unique
• Be premium looking, including colors
• OK to explore a vintage tractor, image of a rooster, family farm, as a couple of ideas.
• Open to all ideas; do not be limited to the above ideas
• Should not look like a generic bag of potatoes

```html
<!DOCTYPE html>
<html lang="en">
<head>
<meta charset="utf-8">
<title>Brennick Bros – Premium Tovelin Potatoes, bag colourways</title>
<link rel="stylesheet" href="https://fonts.googleapis.com/css2?family=Marcellus+SC&display=swap">
<style>
  :root {
    --canvas: #ffffff;
    --earth-band: #433632;
    --earth-stripe-a: #e2dcd3;
    --earth-stripe-b: #ece9e6;
    --earth-brand: #433632;
    --earth-tagline: #433632;
    --meadow-band: #5e9a0a;
    --meadow-stripe-a: #d9e4c9;
    --meadow-stripe-b: #f3f3ef;
    --meadow-brand: #8fab5c;
    --meadow-tagline: #5e9a0a;
    --harbour-band: #3b4a6b;
    --harbour-stripe-a: #c9bdb0;
    --harbour-stripe-b: #eac6a8;
    --harbour-brand: #3b4a6b;
    --harbour-tagline: #3b4a6b;
    --window-edge: #ffffff;
    --produce-light: #e8b83a;
    --produce-mid: #c99520;
    --produce-dark: #6b4a14;
  }
  * { margin: 0; padding: 0; box-sizing: border-box; }
  html, body {
    width: 1200px;
    height: 788px;
    overflow: hidden;
    background: var(--canvas);
  }
  .colourways {
    position: relative;
    width: 1200px;
    height: 788px;
  }
  .bag-face {
    position: absolute;
    top: 121px;
    width: 272px;
    height: 545px;
    background: repeating-linear-gradient(
      to right,
      var(--stripe-a) 0 16px,
      var(--stripe-b) 16px 32px
    );
    font-family: "Marcellus SC", serif;
    text-align: center;
  }
  .bag-face--earth {
    left: 109px;
    --band: var(--earth-band);
    --stripe-a: var(--earth-stripe-a);
    --stripe-b: var(--earth-stripe-b);
    --brand: var(--earth-brand);
    --tagline: var(--earth-tagline);
  }
  .bag-face--meadow {
    left: 464px;
    --band: var(--meadow-band);
    --stripe-a: var(--meadow-stripe-a);
    --stripe-b: var(--meadow-stripe-b);
    --brand: var(--meadow-brand);
    --tagline: var(--meadow-tagline);
  }
  .bag-face--harbour {
    left: 819px;
    --band: var(--harbour-band);
    --stripe-a: var(--harbour-stripe-a);
    --stripe-b: var(--harbour-stripe-b);
    --brand: var(--harbour-brand);
    --tagline: var(--harbour-tagline);
  }
  .tear-strip,
  .base-band {
    position: absolute;
    left: 0;
    width: 100%;
    height: 28px;
    background: var(--band);
  }
  .tear-strip { top: 0; }
  .base-band { bottom: 0; }
  .brand-name {
    position: absolute;
    top: 62px;
    left: 0;
    width: 100%;
    color: var(--brand);
    font-size: 50px;
    line-height: 62px;
    font-weight: 400;
  }
  .brand-name span { display: block; }
  .product-name {
    position: absolute;
    top: 214px;
    left: 0;
    width: 100%;
    color: var(--tagline);
    font-size: 20px;
    line-height: 27px;
    letter-spacing: 0.5px;
  }
  .product-name span { display: block; }
  .product-window {
    position: absolute;
    top: 294px;
    left: 96px;
    width: 80px;
    height: 168px;
    border-radius: 40px;
    border: 1px solid var(--window-edge);
    background:
      radial-gradient(ellipse at 40% 30%, var(--produce-light) 0%, transparent 55%),
      radial-gradient(ellipse at 60% 75%, var(--produce-light) 0%, transparent 50%),
      linear-gradient(160deg, var(--produce-mid) 0%, var(--produce-dark) 45%, var(--produce-mid) 100%);
  }
</style>
</head>
<body>
  <main class="colourways">
    <section class="bag-face bag-face--earth" aria-label="Bag face, earth brown colourway">
      <div class="tear-strip"></div>
      <h1 class="brand-name"><span>Brennick</span><span>Bros</span></h1>
      <p class="product-name"><span>Premium Tovelin</span><span>Potatoes</span></p>
      <div class="product-window" role="img" aria-label="Window showing potatoes behind yellow netting"></div>
      <div class="base-band"></div>
    </section>

    <section class="bag-face bag-face--meadow" aria-label="Bag face, meadow green colourway">
      <div class="tear-strip"></div>
      <h2 class="brand-name"><span>Brennick</span><span>Bros</span></h2>
      <p class="product-name"><span>Premium Tovelin</span><span>Potatoes</span></p>
      <div class="product-window" role="img" aria-label="Window showing potatoes behind yellow netting"></div>
      <div class="base-band"></div>
    </section>

    <section class="bag-face bag-face--harbour" aria-label="Bag face, harbour blue colourway">
      <div class="tear-strip"></div>
      <h2 class="brand-name"><span>Brennick</span><span>Bros</span></h2>
      <p class="product-name"><span>Premium Tovelin</span><span>Potatoes</span></p>
      <div class="product-window" role="img" aria-label="Window showing potatoes behind yellow netting"></div>
      <div class="base-band"></div>
    </section>
  </main>
</body>
</html>
```